Velmi Corporate Website for technological company

We need a modern website to promote our product and services.
You can found the actually website at the address: www.velmi-example.ch

We are a new company for B2B market. We would like do show our high precision and innovation capability.

we need a section were is possible to easily upload "news" and documents for our customers.

Target Market(s)

B2B services in the industry market

Industry/Entity Type

It Company

Coding

Coded - Design and coding required

Number of Pages Required

5+ page

Font styles to use
Other font styles liked:
• We accept propositions

Requirements
Must have
• Easy to maintain
• Presentation of the Velmi company
• Presentation of Velmi services and products
• The customer can download our ducumentation
Nice to have
• Sexy and modern

```html
<!DOCTYPE html>
<html lang="en">
<head>
<meta charset="utf-8">
<title>Velmi Control Systems</title>
<link rel="stylesheet" href="https://fonts.googleapis.com/css2?family=Exo+2:wght@500;600;700&family=Open+Sans:wght@400;600;700&display=swap">
<style>
:root{
  --gold:#a3975a;
  --gold-dark:#877b3d;
  --ink:#2c2c2c;
  --text:#444;
  --muted:#bdbdbd;
  --dark:#2a2a2a;
  --darker:#1f1f1f;
  --light:#f0f0f0;
  --line:#d9d9d9;
  --white:#fff;
}
*{margin:0;padding:0;box-sizing:border-box}
html,body{width:1200px;height:3072px;overflow:hidden;background:var(--white)}
body{position:relative;font-family:"Open Sans",Arial,sans-serif;color:var(--text)}
.abs{position:absolute}
.heading{font-family:"Exo 2",Arial,sans-serif;font-weight:600;color:var(--ink);letter-spacing:.5px}
.btn{position:absolute;display:flex;align-items:center;justify-content:center;background:linear-gradient(var(--gold),var(--gold-dark));color:var(--white);font-family:"Open Sans",sans-serif;font-weight:700;font-size:14px;letter-spacing:.5px;text-transform:uppercase}

/* header */
.topbar{left:676px;top:0;width:450px;height:57px}
.topbar-items{left:700px;top:0;width:400px;height:50px;display:flex;align-items:center;justify-content:space-around;color:#ddd;font-size:12px}
.topbar-items .dot{display:inline-block;width:9px;height:9px;border-radius:50%;background:var(--gold);margin-right:6px;vertical-align:middle}
.logo{left:80px;top:72px;display:flex;align-items:center;gap:12px;font-family:"Exo 2",sans-serif;font-weight:700;font-size:44px;color:var(--ink);letter-spacing:1px}
.logo .mark{width:30px;height:30px;background:var(--gold)}
.nav{left:481px;top:82px;display:flex;height:39px;align-items:center;font-family:"Exo 2",sans-serif;font-weight:600;font-size:15px;color:var(--ink)}
.nav a{text-decoration:none;color:inherit;padding:0 24px}
.nav a.active{background:var(--gold);color:var(--white);height:39px;display:flex;align-items:center;padding:0 18px}

/* hero */
.hero{left:0;top:131px;width:1200px;height:596px;background:linear-gradient(180deg,#6c6a66 0%,#4a4846 45%,#2e2d2c 100%)}
.hero-title{left:0;top:290px;width:1200px;text-align:center;font-family:"Exo 2",sans-serif;font-weight:600;font-size:62px;color:var(--white);letter-spacing:1px}
.hero-sub{left:140px;top:378px;width:920px;text-align:center;font-size:18px;line-height:34px;color:var(--white)}
.hero-btn{left:530px;top:473px;width:140px;height:54px;border:2px solid var(--white);color:var(--white);font-size:17px;display:flex;align-items:center;justify-content:center}
.dots{left:532px;top:651px;display:flex;gap:8px}
.dots span{width:20px;height:20px;border-radius:50%;border:2px solid var(--white)}
.dots span.on{background:var(--gold);border-color:var(--white)}

/* welcome */
.welcome{left:74px;top:764px;width:690px}
.welcome h2{font-size:27px;margin-bottom:20px}
.welcome p{font-size:15px;line-height:23.5px;margin-bottom:14px}
.welcome .lead{color:var(--gold-dark);font-weight:700;margin-bottom:12px}
.areas{list-style:none}
.areas li{font-size:15px;line-height:32px;display:flex;align-items:center;gap:12px}
.areas li svg{flex:none}
.download-box{left:795px;top:770px;width:331px;height:66px;background:linear-gradient(#3b3b3b,#262626);display:flex;align-items:center;gap:18px;padding-left:22px;color:var(--white);font-family:"Exo 2",sans-serif;font-weight:600;font-size:19px;line-height:22px}
.news{left:795px;top:852px;width:331px;height:412px;background:var(--light);padding:24px 26px}
.news h3{font-size:27px;margin-bottom:14px}
.news .date{font-family:"Exo 2",sans-serif;font-weight:600;font-size:14px;color:var(--gold-dark);margin-bottom:8px}
.news p{font-size:15px;line-height:22px;color:var(--text)}
.news hr{border:0;border-top:1px solid var(--line);margin:22px 0 20px}

/* services */
.services{left:0;top:1311px;width:1200px;height:487px;background:var(--dark)}
.services h2{position:absolute;top:44px;width:1200px;text-align:center;color:var(--white);font-size:28px}
.service{position:absolute;top:110px;width:250px;text-align:center}
.service .icon{height:80px;display:flex;align-items:center;justify-content:center}
.service h4{font-family:"Exo 2",sans-serif;font-weight:600;font-size:18px;color:var(--gold);margin:22px 0 8px;letter-spacing:.5px}
.service p{font-size:14px;line-height:23px;color:var(--muted)}

/* products */
.products-title{left:74px;top:1830px;font-size:27px}
.tab{left:74px;width:180px;height:47px;display:flex;align-items:center;padding-left:30px;font-family:"Exo 2",sans-serif;font-weight:600;font-size:13px}
.tab.idle{top:1894px;background:var(--light);color:var(--ink);border:1px solid var(--line)}
.tab.current{top:1948px;background:linear-gradient(var(--gold),var(--gold-dark));color:var(--white)}
.product-panel{left:252px;top:1894px;width:874px;height:328px;background:var(--light);border:1px solid var(--line)}
.product-name{left:430px;top:1924px;font-family:"Exo 2",sans-serif;font-weight:700;font-size:24px;color:var(--gold-dark);line-height:26px}
.product-tag{left:430px;top:1954px;font-family:"Exo 2",sans-serif;font-weight:700;font-size:14px;color:var(--ink)}
.product-rule{left:279px;top:1976px;width:240px;height:2px;background:var(--ink)}
.product-text{left:279px;top:1988px;width:490px;font-size:15px;line-height:24.5px;color:var(--text)}
.product-image{left:788px;top:1929px;width:314px;height:258px;background:#fff;border:1px solid var(--line);display:flex;align-items:center;justify-content:center}
.product-image div{width:260px;height:200px;background:linear-gradient(135deg,#4f7a55,#2f4f39 60%,#5aa06a);border-radius:6px}

/* motion */
.motion{left:0;top:2273px;width:1200px;height:467px;background:var(--dark)}
.motion h2{position:absolute;left:59px;top:56px;font-family:"Exo 2",sans-serif;font-weight:600;font-size:33px;color:var(--white)}
.motion ul{position:absolute;left:59px;top:120px;list-style:none;width:620px}
.motion li{display:flex;gap:14px;font-size:17px;line-height:37.5px;color:#e6e6e6}
.motion li svg{flex:none;margin-top:7px}
.motion .cont{padding-left:38px}
.brochure{left:682px;top:2324px;width:457px;height:359px;background:linear-gradient(180deg,#f4f4f4,#dcdcdc);box-shadow:0 4px 12px rgba(0,0,0,.4)}

/* footer */
.footer{left:0;top:2740px;width:1200px;height:332px;background:var(--darker)}
.footer-logo{left:45px;top:2850px;display:flex;align-items:center;gap:12px;font-family:"Exo 2",sans-serif;font-weight:700;font-size:44px;color:var(--white)}
.footer-logo .mark{width:30px;height:30px;background:var(--gold)}
.footer h5{position:absolute;top:36px;font-family:"Open Sans",sans-serif;font-weight:700;font-size:18px;color:var(--white);letter-spacing:.5px}
.contact-list{left:399px;top:2826px;list-style:none}
.contact-list li{display:flex;gap:16px;font-size:13px;line-height:31px;color:#ddd}
.contact-list li svg{flex:none;margin-top:10px}
.contact-list .addr{line-height:17px;margin-top:7px}
.newsletter{left:637px;top:2823px;width:225px;font-size:13px;line-height:21px;color:#ddd}
.newsletter .field{margin-top:16px;width:225px;height:36px;background:var(--white);color:#666;font-size:13px;display:flex;align-items:center;padding-left:12px}
.newsletter .btn{position:static;margin-top:12px;width:86px;height:28px;font-size:11px}
.follow{left:903px;top:2823px;width:230px;font-size:13px;line-height:21px;color:#ddd}
.socials{left:903px;top:2905px;display:flex;gap:7px}
.socials span{width:40px;height:40px;border-radius:50%;border:2px solid var(--white)}
.copyright{left:0;top:3024px;width:1200px;text-align:center;font-size:13px;color:#ddd}
</style>
</head>
<body>

<!-- header -->
<svg class="abs topbar" width="450" height="57" viewBox="0 0 450 57"><path d="M0 0H450L430 57H20Z" fill="#1f1f1f"/></svg>
<div class="abs topbar-items"><span><span class="dot"></span>+41 (0)21 555 01 23 ⌄</span><span>MEMBER LOG IN ⌄</span><span>EN ⌄</span></div>
<div class="abs logo"><span class="mark"></span>VELMI</div>
<nav class="abs nav"><a class="active">HOME</a><a>SERVICES</a><a>PRODUCTS</a><a>EXAMPLES</a><a>DOWNLOAD</a><a>CONTACTS</a></nav>

<!-- hero -->
<div class="abs hero" role="img" aria-label="Photo of a team working together at a meeting table"></div>
<svg class="abs" style="left:0;top:660px" width="1200" height="68" viewBox="0 0 1200 68"><path d="M0 8Q600 110 1200 8V68H0Z" fill="#fff"/></svg>
<h1 class="abs hero-title">VELMI CONTROL SYSTEMS</h1>
<p class="abs hero-sub">VELMI Ltd. designs systems in which electronics, software and mechanics are perfectly integrated to achieve uncompromising performance.</p>
<div class="abs hero-btn">Read More</div>
<div class="abs dots"><span class="on"></span><span></span><span></span><span></span><span></span></div>

<!-- welcome -->
<section class="abs welcome">
  <h2 class="heading">WELCOME TO OUR WEBSITE</h2>
  <p>The ever-increasing complexity in modern systems, the search for reliability and performance and the continuous desire to reduce production costs and dimensions of the products require a rigorous integration between the electronic units, software and mechanical systems.</p>
  <p>VELMI Ltd. designs systems in which electronics, software and mechanics are perfectly integrated to achieve uncompromising performance.</p>
  <p>VELMI Ltd. designs systems in which electronics, software and mechanics are perfectly integrated to achieve uncompromising performance.</p>
  <p class="lead">VELMI Ltd. is a company active in the following areas:</p>
  <ul class="areas">
    <li><svg width="14" height="14" viewBox="0 0 14 14"><circle cx="7" cy="7" r="7" fill="#a3975a"/><path d="M3.5 7.2l2.3 2.3 4.7-4.7" stroke="#fff" stroke-width="1.8" fill="none"/></svg>Simulation and modeling of complete processes</li>
    <li><svg width="14" height="14" viewBox="0 0 14 14"><circle cx="7" cy="7" r="7" fill="#a3975a"/><path d="M3.5 7.2l2.3 2.3 4.7-4.7" stroke="#fff" stroke-width="1.8" fill="none"/></svg>Concept and design of electronic circuits and mechanical units</li>
    <li><svg width="14" height="14" viewBox="0 0 14 14"><circle cx="7" cy="7" r="7" fill="#a3975a"/><path d="M3.5 7.2l2.3 2.3 4.7-4.7" stroke="#fff" stroke-width="1.8" fill="none"/></svg>Development of application specific control software</li>
    <li><svg width="14" height="14" viewBox="0 0 14 14"><circle cx="7" cy="7" r="7" fill="#a3975a"/><path d="M3.5 7.2l2.3 2.3 4.7-4.7" stroke="#fff" stroke-width="1.8" fill="none"/></svg>Rapid prototyping (electronic cards, mechanisms ...)</li>
  </ul>
</section>
<div class="btn" style="left:74px;top:1221px;width:151px;height:45px">Read more</div>

<div class="abs download-box">
  <svg width="34" height="34" viewBox="0 0 34 34"><rect x="2" y="22" width="30" height="10" fill="#a3975a"/><path d="M17 2v18M9 13l8 8 8-8" stroke="#a3975a" stroke-width="5" fill="none"/></svg>
  <span>DOWNLAOD<br>BROCHURE VELMI <small style="font-size:13px">(EN)</small></span>
</div>
<aside class="abs news">
  <h3 class="heading">LATEST NEWS</h3>
  <div class="date">OCT 16, 2016</div>
  <p>The Velmi team will be present at the stand A16 of Indutech exhibition in Bern, between 6 and 8 september 2016.</p>
  <hr>
  <div class="date">OCT 16, 2016</div>
  <p>Added the 'application' page, showing some of the developments of Velmi Ltd...</p>
</aside>
<div class="btn" style="left:821px;top:1194px;width:150px;height:43px">Read all news</div>

<!-- services -->
<section class="abs services">
  <h2 class="heading">OUR SERVICES</h2>
  <div class="service" style="left:72px">
    <div class="icon"><svg width="64" height="64" viewBox="0 0 64 64" fill="none" stroke="#fff" stroke-width="4"><rect x="12" y="12" width="40" height="40" rx="4"/><rect x="21" y="21" width="22" height="22" fill="#fff"/><path d="M20 4v8M28 4v8M36 4v8M44 4v8M20 52v8M28 52v8M36 52v8M44 52v8M4 20h8M4 28h8M4 36h8M4 44h8M52 20h8M52 28h8M52 36h8M52 44h8"/></svg></div>
    <h4>ELECTRONICS</h4>
    <p>VELMI Sàrl being active in all fields associated with actuator electronics, can develop solutions integrating...</p>
  </div>
  <div class="service" style="left:342px">
    <div class="icon"><svg width="64" height="64" viewBox="0 0 64 64"><g fill="#fff"><circle cx="32" cy="32" r="21"/><rect x="26" y="2" width="12" height="14"/><rect x="26" y="48" width="12" height="14"/><rect x="2" y="26" width="14" height="12"/><rect x="48" y="26" width="14" height="12"/><rect x="26" y="2" width="12" height="14" transform="rotate(45 32 32)"/><rect x="26" y="48" width="12" height="14" transform="rotate(45 32 32)"/><rect x="2" y="26" width="14" height="12" transform="rotate(45 32 32)"/><rect x="48" y="26" width="14" height="12" transform="rotate(45 32 32)"/></g><circle cx="32" cy="32" r="8" fill="#2a2a2a"/></svg></div>
    <h4>MECHANICS</h4>
    <p>VELMI Sàrl being active in all fields associated with actuator electronics, can develop solutions integrating...</p>
  </div>
  <div class="service" style="left:608px">
    <div class="icon"><svg width="76" height="56" viewBox="0 0 76 56" fill="none" stroke="#fff" stroke-width="4"><rect x="12" y="4" width="52" height="36" rx="3"/><path d="M2 48h72v4H2z" fill="#fff"/></svg></div>
    <h4>SOFTWARE</h4>
    <p>VELMI Sàrl being active in all fields associated with actuator electronics, can develop solutions integrating...</p>
  </div>
  <div class="service" style="left:879px">
    <div class="icon"><svg width="100" height="70" viewBox="0 0 100 70" fill="none" stroke="#fff" stroke-width="4"><rect x="8" y="4" width="84" height="54" rx="4"/><path d="M2 64h96"/><path d="M38 22l12-6 12 6v16l-12 6-12-6zM38 22l12 6 12-6M50 28v16" stroke-width="3"/></svg></div>
    <h4>SIMULATION &amp; MODELING</h4>
    <p>VELMI Sàrl being active in all fields associated with actuator electronics, can develop solutions integrating...</p>
  </div>
  <div class="btn" style="left:498px;top:389px;width:205px;height:47px">View all services</div>
</section>

<!-- products -->
<h2 class="abs heading products-title">OUR PRODUCTS</h2>
<div class="abs product-panel"></div>
<div class="abs tab idle">MOTOR DRIVER</div>
<div class="abs tab current">BUS INTERFACE</div>
<div class="abs product-name">PETREL:</div>
<div class="abs product-tag">INTELLIGENT CONTROL FOR ELECTRIC MOTORS</div>
<div class="abs product-rule"></div>
<p class="abs product-text">Petrel is an electronics board developed for the control of DC and BLDC motors with a power ranging from 1W to 250W. This board integrates a powerful ARM processor, a power stage, two communication buses, a number of interfaces compatible with the different position sensor standards available on the market...</p>
<div class="btn" style="left:279px;top:2142px;width:196px;height:45px">View all product</div>
<div class="abs product-image"><div role="img" aria-label="Photo of the green motor control circuit board with connectors"></div></div>

<!-- intelligent motion -->
<section class="abs motion">
  <h2>Velmi Intelligent Motion</h2>
  <ul>
    <li><svg width="22" height="22" viewBox="0 0 22 22" fill="none" stroke="#fff" stroke-width="2"><rect x="1" y="3" width="17" height="17"/><path d="M5 11l4 4 12-13"/></svg>Automatic dispenser for easily degradable organic products.</li>
    <li><svg width="22" height="22" viewBox="0 0 22 22" fill="none" stroke="#fff" stroke-width="2"><rect x="1" y="3" width="17" height="17"/><path d="M5 11l4 4 12-13"/></svg>Validation system of the lifetime and the wear of ball bearings.</li>
    <li class="cont">positioning system spheres steel or carbon fibers.</li>
    <li><svg width="22" height="22" viewBox="0 0 22 22" fill="none" stroke="#fff" stroke-width="2"><rect x="1" y="3" width="17" height="17"/><path d="M5 11l4 4 12-13"/></svg>Pump control system with integrated self-diagnosis.</li>
    <li><svg width="22" height="22" viewBox="0 0 22 22" fill="none" stroke="#fff" stroke-width="2"><rect x="1" y="3" width="17" height="17"/><path d="M5 11l4 4 12-13"/></svg>Integrated turbo control with self-diagnosis.</li>
    <li><svg width="22" height="22" viewBox="0 0 22 22" fill="none" stroke="#fff" stroke-width="2"><rect x="1" y="3" width="17" height="17"/><path d="M5 11l4 4 12-13"/></svg>Capture system and angular positioning of a shaft.</li>
  </ul>
  <div class="btn" style="left:59px;top:361px;width:205px;height:43px">Download our PDF</div>
</section>
<div class="abs brochure" role="img" aria-label="Three overlapping application brochure pages with product photos and green highlight boxes"></div>

<!-- footer -->
<footer class="abs footer">
  <h5 style="left:399px">CONTACT US</h5>
  <h5 style="left:637px">NEWSLETTER</h5>
  <h5 style="left:903px">FOLLOW US</h5>
</footer>
<div class="abs footer-logo"><span class="mark"></span>VELMI</div>
<ul class="abs contact-list">
  <li><svg width="14" height="12" viewBox="0 0 14 12"><path d="M1 3q6-4 12 0v2h-3V4H4v1H1zM2 6h10v6H2z" fill="#fff"/></svg>+41 (0)21 555 01 23 (Phone)</li>
  <li><svg width="14" height="12" viewBox="0 0 14 12"><rect x="1" y="4" width="12" height="8" fill="#fff"/><rect x="3" y="0" width="8" height="4" fill="#fff"/></svg>+41 (0)21 555 01 24 (Fax)</li>
  <li><svg width="14" height="11" viewBox="0 0 14 11"><rect x="0" y="0" width="14" height="11" fill="#fff"/><path d="M0 0l7 6 7-6" stroke="#1f1f1f" fill="none"/></svg><span style="text-decoration:underline">info@velmi-example.ch (Email)</span></li>
  <li><svg width="14" height="14" viewBox="0 0 14 14"><path d="M7 0a5 5 0 0 1 5 5c0 4-5 9-5 9S2 9 2 5a5 5 0 0 1 5-5z" fill="#fff"/><circle cx="7" cy="5" r="2" fill="#1f1f1f"/></svg><span class="addr">Chemin des Vergers 8<br>CH - 1700 Sampleville</span></li>
</ul>
<div class="abs newsletter">
  Register Your email address to get information ablout us
  <div class="field">Email Address</div>
  <div class="btn">Subscribe</div>
</div>
<p class="abs follow">Lorem ipsum dolor sit amet, conse ctetur adipiscing elit. Nulla in purus nibh. Donec ornare</p>
<div class="abs socials"><span></span><span></span><span></span><span></span><span></span></div>
<p class="abs copyright">Copyright © velmi. All rights reserved</p>

</body>
</html>
```